Business card revamp

we are refrigeration mechanic i need a modern professional double side business card using my current branding
The card information must have site address~ 17 Whitlow st Wendara, Vic 3712 postal address~ P.o. Box 862 Wendara,Vic 3713 Phone Number~0358149637 Fax Nunber~0358260518 Email address~ brucet@pelvanor.com.au Title~ Manager Licence numbers~ AU47391, NSW 681329K Web site~ www.frostrimvane.com.au

Industry/Entity Type

Business

```html
<!DOCTYPE html>
<html lang="en">
<head>
<meta charset="utf-8">
<title>Frostrim Vane – Business Card</title>
<link rel="stylesheet" href="https://fonts.googleapis.com/css2?family=Montserrat:wght@500;600;700&display=swap">
<style>
  :root {
    --stage: #3d4543;
    --card: #fbfbfa;
    --brand-red: #c0242c;
    --brand-blue: #1f6fb8;
    --ink: #2f3133;
    --band-title: #e9a9ac;
    --flourish-blue: rgba(31,111,184,.22);
    --flourish-red: rgba(210,110,90,.22);
  }
  * { box-sizing: border-box; margin: 0; padding: 0; }
  html, body {
    width: 1200px; height: 900px; overflow: hidden;
    background: var(--stage);
    font-family: "Montserrat", sans-serif;
  }
  .sheet {
    position: relative; width: 1200px; height: 900px;
    display: flex; flex-direction: column; align-items: center;
    justify-content: center; gap: 60px;
  }
  .card {
    position: relative; width: 700px; height: 400px;
    background: var(--card);
    box-shadow: 0 10px 30px rgba(0,0,0,.35);
    overflow: hidden;
  }
  .brand { display: flex; flex-direction: column; align-items: center; }
  .brand-row { display: flex; align-items: center; gap: 14px; }
  .brand-mark {
    width: 20px; height: 20px; border-radius: 50%;
    background: var(--brand-blue);
  }
  .brand-name {
    font-weight: 700; font-size: 42px; letter-spacing: 1px;
    color: var(--brand-blue); text-transform: uppercase; line-height: 1;
  }
  .brand-tagline {
    margin-top: 10px; font-weight: 500; font-size: 12px;
    letter-spacing: 2px; color: var(--ink); text-transform: uppercase;
  }

  /* front */
  .card-front .brand { padding-top: 64px; }
  .name-band {
    position: absolute; left: 0; right: 0; top: 178px; height: 68px;
    background: var(--brand-red);
    display: flex; flex-direction: column; align-items: center; justify-content: center;
  }
  .person-name {
    color: #fff; font-weight: 600; font-size: 20px; letter-spacing: 3px;
    text-transform: uppercase; line-height: 1.2;
  }
  .person-title {
    color: var(--band-title); font-weight: 600; font-size: 13px; letter-spacing: 1.5px;
    margin-top: 2px;
  }
  .contact {
    position: absolute; left: 0; right: 0; top: 272px;
    text-align: center; color: var(--ink); font-style: normal;
    font-weight: 500; font-size: 15px; line-height: 25px; letter-spacing: .6px;
  }

  /* back */
  .card-back { display: flex; align-items: center; justify-content: center; }
  .edge-flourish {
    position: absolute; left: 22px; top: 0; width: 46px; height: 400px;
    background: linear-gradient(180deg, var(--flourish-blue), var(--flourish-red) 50%, var(--flourish-blue));
    border-radius: 23px;
  }
</style>
</head>
<body>
<main class="sheet">
  <section class="card card-front" aria-label="Card front">
    <div class="brand">
      <div class="brand-row">
        <span class="brand-mark"></span>
        <span class="brand-name">Frostrim Vane</span>
      </div>
      <p class="brand-tagline">Heating and cooling specialists</p>
    </div>
    <div class="name-band">
      <p class="person-name">Marcus Delroy</p>
      <p class="person-title">Manager</p>
    </div>
    <address class="contact">
      17 Whitlow st Wendara, Vic 3712; P.o. Box 862 Wendara,Vic 3713<br>
      Licence numbers: AU47391, NSW 681329K<br>
      P: 0358149637 | F: 0358260518<br>
      E: brucet@pelvanor.com.au | www.frostrimvane.com.au
    </address>
  </section>

  <section class="card card-back" aria-label="Card back">
    <div class="edge-flourish" role="img" aria-label="Faint blue and red flowing air decoration along the card edge"></div>
    <div class="brand">
      <div class="brand-row">
        <span class="brand-mark"></span>
        <span class="brand-name">Frostrim Vane</span>
      </div>
      <p class="brand-tagline">Heating and cooling specialists</p>
    </div>
  </section>
</main>
</body>
</html>
```